K SPIRES Business Card Design

Need a business card design for K Spires, we're a tower company - our main scope of work is to upgrade cellular sites: swap antennas, install new coax, fiber, replace mounts, etc. Mostly tower work.

would like to see a sharp business card design with our logo either on background or with tower image on the background - something describing our field not only in words but in images.

Target Market(s)

USA

Industry/Entity Type

Business

Contact Information for Business Card

Tarik Benolven
Operations Manager
K Spires LLC

cell 404-555-0193
tarik@k-spires-example.com

2150 Harlowe Commerce Pkwy, Suite D
Norcross, GA, 30099

Requirements
Must have
• some tower related design
Nice to have
• some tower or cellular antennas on the background, if possible to compliment our logo...

```html
<!DOCTYPE html>
<html lang="en">
<head>
<meta charset="utf-8">
<title>K Spires Business Card</title>
<link rel="stylesheet" href="https://fonts.googleapis.com/css2?family=Source+Sans+3:wght@400;600&display=swap">
<style>
  :root {
    --backdrop: #2b2b2b;
    --card-white: #ffffff;
    --brand-green: #378b41;
    --brand-green-text: #2e8a3b;
    --brand-green-faint: #5db56a;
    --brand-navy: #2b2a7c;
    --text-grey: #6a6a6a;
  }
  * { margin: 0; padding: 0; box-sizing: border-box; }
  html, body {
    width: 1200px; height: 900px; overflow: hidden;
    background: var(--backdrop);
    font-family: "Source Sans 3", sans-serif;
  }
  .canvas { position: relative; width: 1200px; height: 900px; }
  .card {
    position: absolute;
    width: 542px; height: 314px;
    border-radius: 18px;
    overflow: hidden;
  }
  .card--front { left: 334px; top: 101px; background: var(--card-white); }
  .card--back { left: 334px; top: 487px; background: var(--brand-green); }

  .tower-art {
    position: absolute;
    border-radius: 4px;
  }
  .tower-art--front {
    left: 400px; top: 22px; width: 110px; height: 140px;
    background: linear-gradient(180deg, rgba(55,139,65,0.10), rgba(43,42,124,0.10));
  }
  .tower-art--back {
    left: 221px; top: 36px; width: 100px; height: 240px;
    background: linear-gradient(180deg, rgba(93,181,106,0.35), rgba(93,181,106,0.12));
  }

  .wordmark {
    position: absolute; left: 23px; top: 40px;
    font-size: 50px; font-weight: 600; line-height: 1;
    color: var(--brand-navy);
    display: flex; align-items: center; gap: 10px;
  }
  .wordmark__square {
    width: 18px; height: 18px; background: var(--brand-navy);
  }
  .address {
    position: absolute; left: 23px; top: 173px;
    font-size: 16.5px; line-height: 17px; color: var(--text-grey);
  }
  .contact-list {
    position: absolute; left: 22px; top: 229px;
    list-style: none;
    font-size: 16.5px; line-height: 20.5px; color: var(--brand-green-text);
  }
  .contact-list li { display: flex; align-items: center; gap: 7px; }
  .contact-list svg { width: 12px; height: 12px; fill: var(--brand-navy); }
  .person {
    position: absolute; right: 24px; top: 182px; text-align: right;
  }
  .person__name {
    font-size: 24.5px; font-weight: 600; color: var(--brand-navy); line-height: 27px;
  }
  .person__title {
    font-size: 17px; color: var(--brand-green-text); line-height: 20px;
  }
  .back-mark {
    position: absolute; left: 0; right: 0; top: 108px;
    text-align: center;
    font-size: 92px; font-weight: 600; line-height: 1;
    color: var(--brand-green-faint);
  }
</style>
</head>
<body>
<div class="canvas">
  <section class="card card--front">
    <div class="tower-art tower-art--front" role="img" aria-label="Cell tower with antennas illustration"></div>
    <div class="wordmark"><span class="wordmark__square"></span>K Spires</div>
    <p class="address">2150 Harlowe Commerce Pkwy, Suite D<br>Norcross, GA, 30099</p>
    <ul class="contact-list">
      <li><svg viewBox="0 0 12 12" aria-hidden="true"><path d="M1 3c0-1 1-2 5-2s5 1 5 2v1H8V3H4v1H1z M3 5h6l2 5H1z"/></svg>404-555-0193</li>
      <li><svg viewBox="0 0 12 12" aria-hidden="true"><path d="M1 3h10v6H1z" fill="none" stroke="#2b2a7c" stroke-width="1.4"/><path d="M1 3l5 4 5-4"/></svg>tarik@k-spires-example.com</li>
    </ul>
    <div class="person">
      <p class="person__name">Tarik Benolven</p>
      <p class="person__title">Operations Manager</p>
    </div>
  </section>
  <section class="card card--back">
    <div class="tower-art tower-art--back" role="img" aria-label="Faint cell tower illustration"></div>
    <div class="back-mark">K Spires</div>
  </section>
</div>
</body>
</html>
```